Belle Journée Weddings and Events

I am a small boutique wedding coordinator, stylist and bridal consultant/coach/assistant. I am based in Brisbane, Australia and my business is geared towards mid range- high end budget bridal couples.
I am after some business cards that are double sided, with the logo on one side and all other information on the other side, including the business tagline of design, create, celebrate. The look of the card needs to be clean and crisp, with white and the tones of grey of the logo.The final design needs to convey sophistication and poise. Perhaps the logo and tagline could be done in a metallic silver with the rest of the text in the shades of grey from the style guide attached below.
Title- Mirela Tostavanque - Director / Events Manager and Stylist
Address - 218 Hollis Terrace, Marwick Vale, QLD, 4067
Phone- 07 3482 9517
Mobile- 0418 572 906
Email- Mirela@bellejourneeevents.com.au
Website- www.bellejourneeevents.com.au

```html
<!DOCTYPE html>
<html lang="en">
<head>
<meta charset="utf-8">
<title>Belle Journée Weddings and Events – Business Card</title>
<link href="https://fonts.googleapis.com/css2?family=Arimo:wght@400;700&family=Pinyon+Script&display=swap" rel="stylesheet">
<style>
  :root {
    --page: #ffffff;
    --card: #ffffff;
    --ink-strong: #7a7a7a;
    --ink-soft: #8e8e8e;
    --ink-label: #8a8a8a;
    --script: #8b8b8b;
    --dot: #a3a3a3;
    --shadow: rgba(0, 0, 0, 0.28);
  }
  html, body {
    margin: 0;
    padding: 0;
    width: 1200px;
    height: 1000px;
    overflow: hidden;
    background: var(--page);
  }
  .canvas {
    position: relative;
    width: 1200px;
    height: 1000px;
    font-family: "Arimo", Arial, sans-serif;
  }
  .card {
    position: absolute;
    background: var(--card);
    box-shadow: 0 8px 24px var(--shadow);
  }
  /* Logo side */
  .card--front {
    left: 45px;
    top: 500px;
    width: 593px;
    height: 347px;
    display: flex;
    align-items: center;
    justify-content: center;
  }
  .brand {
    text-align: center;
    color: var(--ink-strong);
    font-family: "Arimo", Arial, sans-serif;
    font-weight: 400;
    line-height: 1.3;
  }
  .brand__name {
    display: block;
    font-size: 40px;
    letter-spacing: 1px;
  }
  .brand__line {
    display: block;
    font-size: 13px;
    letter-spacing: 2px;
  }
  .brand__tagline {
    display: block;
    margin-top: 10px;
    font-size: 11px;
    letter-spacing: 3px;
    color: var(--ink-soft);
    text-transform: lowercase;
  }
  /* Information side */
  .card--back {
    left: 551px;
    top: 383px;
    width: 612px;
    height: 358px;
  }
  .holder__name {
    position: absolute;
    left: 39px;
    top: 34px;
    margin: 0;
    font-family: "Pinyon Script", cursive;
    font-weight: 400;
    font-size: 44px;
    color: var(--script);
    line-height: 1.1;
  }
  .holder__title {
    position: absolute;
    left: 39px;
    top: 90px;
    margin: 0;
    font-size: 13px;
    color: var(--ink-soft);
  }
  .contact {
    position: absolute;
    left: 39px;
    top: 250px;
    margin: 0;
    font-size: 13px;
    line-height: 16.5px;
    color: var(--ink-soft);
  }
  .contact dt {
    display: inline;
    font-weight: 700;
    color: var(--ink-label);
  }
  .contact dd {
    display: inline;
    margin: 0;
  }
  .contact dd::after {
    content: "";
    display: block;
  }
  .website {
    position: absolute;
    right: 50px;
    top: 298px;
    margin: 0;
    font-size: 13px;
    font-weight: 700;
    color: var(--ink-strong);
  }
  .dot-trail {
    position: absolute;
    left: 552px;
    top: 10px;
  }
</style>
</head>
<body>
<main class="canvas">

  <section class="card card--front" aria-label="Business card, logo side">
    <div class="brand">
      <span class="brand__name">Belle Journée</span>
      <span class="brand__line">Weddings and Events</span>
      <span class="brand__tagline">design, create, celebrate</span>
    </div>
  </section>

  <section class="card card--back" aria-label="Business card, contact side">
    <svg class="dot-trail" width="20" height="105" viewBox="0 0 20 105" aria-hidden="true">
      <circle cx="10" cy="7" r="4" fill="var(--dot)"/>
      <circle cx="10" cy="30" r="3.5" fill="var(--dot)"/>
      <circle cx="10" cy="53" r="3" fill="var(--dot)"/>
      <circle cx="10" cy="76" r="2.5" fill="var(--dot)"/>
      <circle cx="10" cy="98" r="2" fill="var(--dot)"/>
    </svg>

    <h1 class="holder__name">Mirela Tostavanque</h1>
    <p class="holder__title">Director / Events Manager and Stylist</p>

    <dl class="contact">
      <dt>Address:</dt> <dd>218 Hollis Terrace, Marwick Vale, QLD, 4067</dd>
      <dt>Phone:</dt> <dd>07 3482 9517</dd>
      <dt>Mobile</dt>: <dd>0418 572 906</dd>
      <dt>Email</dt>: <dd>Mirela@bellejourneeevents.com.au</dd>
    </dl>

    <p class="website">www.bellejourneeevents.com.au</p>
  </section>

</main>
</body>
</html>
```